Social skills book for children with autism needs a Lumora cover design

We are a small publishing company that produces books for families affected by autism. These books contain lessons that apply theories and techniques used in the clinical setting that parents can use in the comfort of their own homes.

We are currently in the process of producing a book that will initially be released on the Lumora platform that teaches children with autism how to interact positively in a number of different social settings. We are seeking a book cover design with the following characteristics: engaging, brightly-colored, modern, incorporates our logo (see attached), matches the feel of the illustrations in the book (see attached) not kitschy, stands out in the Brightvale Lumora store against similar books.

We would like to see blues and greens used in the design, however, if you think something will work better, please submit as well.

Book Cover Details

Title: Playground Pathways for Little Learners
Author: Delphine Marchetti, Psy.D., BCBA-D
Logo: See attached files
Preferred fonts: Raleway, Palatino (but open to anything)
Optimized for Lumora
Files requested: PDF, original layout files (Illustrator, Indesign, Photoshop, etc.)

Remember to be creative! Since this book is part of a series, there is the potential for other projects in the future if we like your work!

Target Market(s)

Parents and educators of children with autism.

Industry/Entity Type

Publishing Company

Colors

Designer to choose colors to be used in the design.

Requirements
Must have
• Although we have included the illustrations in the design files, please use these only as a reference. We are looking for a design that is original, eye-catching and isn't just an illustration on the cover.

```html
<!DOCTYPE html>
<html lang="en">
<head>
<meta charset="utf-8">
<title>Playground Pathways for Little Learners — Book Cover</title>
<link rel="stylesheet" href="https://fonts.googleapis.com/css2?family=Cinzel:wght@700&family=Marcellus+SC&display=swap">
<style>
  :root {
    --backdrop: #7d9dcf;
    --paper: #ffffff;
    --title-deep: #2b93cf;
    --title-light: #4db3e3;
    --author-ink: #1e3a5c;
    --meadow-glow: #eef2c4;
    --meadow-light: #b9d27e;
    --meadow: #8db552;
    --meadow-deep: #5f8f3a;
    --bark: #9aa58c;
    --hair-warm: #a77a52;
    --skin-warm: #e9c3a6;
    --jacket-teal: #3c7a94;
    --jacket-deep: #2c5f78;
    --plush-gold: #c7974f;
  }
  * { margin: 0; padding: 0; box-sizing: border-box; }
  html, body {
    width: 872px;
    height: 1200px;
    overflow: hidden;
    background: var(--backdrop);
  }
  .book-cover {
    position: absolute;
    left: 16px;
    top: 39px;
    width: 840px;
    height: 1121px;
    background: var(--paper);
    display: flex;
    flex-direction: column;
  }
  .title-block {
    height: 362px;
    padding-top: 40px;
    text-align: center;
    font-family: "Marcellus SC", serif;
    font-weight: 400;
  }
  .title-line {
    display: block;
    font-size: 47px;
    line-height: 56px;
    letter-spacing: 1px;
    color: var(--title-deep);
  }
  .title-line .accent { color: var(--title-light); }
  .title-feature {
    display: block;
    font-size: 112px;
    line-height: 122px;
    letter-spacing: 2px;
    color: var(--title-light);
  }
  .cover-photo {
    height: 624px;
    background:
      radial-gradient(ellipse 22% 18% at 74% 30%, var(--skin-warm) 0%, rgba(233,195,166,0.7) 45%, rgba(233,195,166,0) 100%),
      radial-gradient(ellipse 34% 34% at 76% 26%, var(--hair-warm) 0%, rgba(167,122,82,0.55) 50%, rgba(167,122,82,0) 100%),
      radial-gradient(ellipse 18% 26% at 93% 72%, var(--plush-gold) 0%, rgba(199,151,79,0.75) 50%, rgba(199,151,79,0) 100%),
      radial-gradient(ellipse 36% 34% at 62% 88%, var(--jacket-deep) 0%, var(--jacket-teal) 45%, rgba(60,122,148,0) 100%),
      radial-gradient(ellipse 14% 12% at 14% 22%, var(--meadow-glow) 0%, rgba(238,242,196,0) 100%),
      radial-gradient(ellipse 12% 10% at 36% 14%, var(--meadow-glow) 0%, rgba(238,242,196,0) 100%),
      radial-gradient(ellipse 16% 12% at 30% 60%, rgba(238,242,196,0.8) 0%, rgba(238,242,196,0) 100%),
      radial-gradient(ellipse 6% 45% at 4% 35%, var(--bark) 0%, rgba(154,165,140,0) 100%),
      linear-gradient(180deg, var(--meadow-light) 0%, var(--meadow) 65%, var(--meadow-deep) 100%);
  }
  .author-block {
    height: 135px;
    padding-top: 20px;
    text-align: center;
    font-family: "Cinzel", serif;
    font-weight: 700;
    color: var(--author-ink);
  }
  .author-name {
    font-size: 33px;
    line-height: 40px;
    letter-spacing: 1px;
  }
  .author-credentials {
    font-size: 23px;
    line-height: 30px;
  }
</style>
</head>
<body>
  <main class="book-cover">
    <header class="title-block">
      <h1>
        <span class="title-line">Playground <span class="accent">Pathways</span></span>
        <span class="title-line">For Little</span>
        <span class="title-feature">LEARNERS</span>
      </h1>
    </header>
    <div class="cover-photo" role="img" aria-label="Photograph of a smiling young girl in a teal denim jacket hugging a teddy bear in a sunny green park"></div>
    <footer class="author-block">
      <p class="author-name">Delphine Marchetti</p>
      <p class="author-credentials">Psy.D., BCBA-D</p>
    </footer>
  </main>
</body>
</html>
```